Sports Betting Business Consultant

After 21 years in corporate life. Will be continue as consultant/advisor in sports betting industry. Need a business card. Prefer an Zelvo format as layout. Elements; betting,ticket, sports types soccer, basketball, tennis etc , odds etc.

```html
<!DOCTYPE html>
<html lang="en">
<head>
<meta charset="utf-8">
<title>Your Company – Sports Betting &amp; Tickets</title>
<link rel="stylesheet" href="https://fonts.googleapis.com/css2?family=Lato:wght@400;700&display=swap">
<style>
  :root {
    --card-bg: #050808;
    --brand-blue: #52c8f5;
    --title-white: #ffffff;
    --service-grey: #d3d7d5;
    --web-white: #f4f6f5;
  }
  html, body {
    margin: 0;
    padding: 0;
    width: 720px;
    height: 1200px;
    overflow: hidden;
    background: var(--card-bg);
  }
  .card {
    position: relative;
    width: 720px;
    height: 1200px;
    background: var(--card-bg);
    font-family: "Lato", Arial, sans-serif;
    text-align: center;
  }
  .brand-mark {
    position: absolute;
    left: 290px;
    top: 335px;
    width: 140px;
    height: 140px;
    background: var(--brand-blue);
  }
  .company-name {
    position: absolute;
    left: 0;
    right: 0;
    top: 522px;
    margin: 0;
    font-size: 58px;
    font-weight: 700;
    line-height: 1;
    letter-spacing: 0.5px;
    color: var(--title-white);
  }
  .services {
    position: absolute;
    left: 0;
    right: 0;
    top: 664px;
    margin: 0;
    padding: 0;
    list-style: none;
    font-size: 31px;
    font-weight: 700;
    line-height: 44.8px;
    color: var(--service-grey);
  }
  .website {
    position: absolute;
    left: 0;
    right: 0;
    top: 1047px;
    margin: 0;
    font-size: 23px;
    font-weight: 400;
    line-height: 1.2;
    color: var(--web-white);
  }
</style>
</head>
<body>
  <main class="card">
    <div class="brand-mark" aria-hidden="true"></div>
    <h1 class="company-name">YOUR COMPANY</h1>
    <ul class="services">
      <li>SPORTS BETTING &amp; TICKETS</li>
      <li>SPORT TYPES:</li>
      <li>FOOTBALL</li>
      <li>BASKETBALL</li>
      <li>SOCCER</li>
      <li>TENNIS</li>
      <li>ETC</li>
    </ul>
    <p class="website">www.yourwebsite.com</p>
  </main>
</body>
</html>
```